Torven Medical needs bold attention catching website for healthcare professionals(target)

I need a hero page as well as a products and about page for a website of mine. I specialize in orthopedic instruments . Specifically bone drills and saws. This whole company was founded to bring superb quality highly discounted medical instruments. Specifically bone drills, bone saws, k-wires and pins. Two main points should be cost savings and superior quality.

Target Market(s)

healthcare professionals Surgeons and hospital material managers

Number of Pages Required

3 page

Font styles to use
Serif

Colors

Designer to choose colors to be used in the design.

Requirements
Must have
• colors should match logo design

```html
<!DOCTYPE html>
<html lang="en">
<head>
<meta charset="utf-8">
<title>Torven Medical – Orthopedic Instruments</title>
<link href="https://fonts.googleapis.com/css2?family=Lora:wght@400;500;600;700&display=swap" rel="stylesheet">
<style>
:root{
  --orange:#f7941d;
  --orange-2:#f89f30;
  --orange-3:#f5a843;
  --orange-4:#f3b159;
  --dark:#1e1e1e;
  --ink:#333333;
  --muted:#777777;
  --line:#e4e4e4;
  --pale:#e7e7e7;
  --white:#ffffff;
}
*{margin:0;padding:0;box-sizing:border-box}
html,body{width:1200px;height:4313px;overflow:hidden;background:var(--white)}
body{position:relative;font-family:'Lora',serif;color:var(--ink)}
.abs{position:absolute}
.center{text-align:center}
.small{font-size:11px;line-height:20px;color:var(--muted)}

/* header */
.logo{left:189px;top:22px;font-size:20px;font-weight:600;color:var(--orange);display:flex;align-items:center;gap:8px}
.logo .mark{width:14px;height:14px;border-radius:50%;background:var(--orange)}
.info{display:flex;align-items:center;gap:10px;top:22px}
.info .ico{width:36px;height:36px;border-radius:50%;background:var(--orange);display:flex;align-items:center;justify-content:center;flex:none}
.info b{display:block;font-size:9px;font-weight:700;color:var(--ink)}
.info span{font-size:9px;color:var(--muted)}
.topline{left:189px;top:76px;width:838px;height:1px;background:var(--line)}
.nav{left:189px;top:96px;display:flex;gap:26px;font-size:13px;color:#555}
.nav .active{color:var(--ink);font-weight:700}
.social{display:flex;gap:12px;align-items:center}
.social i{display:block;width:12px;height:12px;border-radius:50%;background:var(--ink)}
.social.orange i{background:var(--orange)}
.social.white i{background:var(--white)}

/* hero */
.hero{left:42px;top:136px;width:1117px;height:448px;background:linear-gradient(100deg,#6b8fc4 0%,#a9c3e3 30%,#e9d7cc 60%,#f4c2a0 100%)}
.hero h1{left:600px;top:118px;width:460px;font-size:33px;font-weight:500;line-height:41px;color:#2b2b2b;text-align:center}
.hero p{left:670px;top:218px;width:320px;font-size:11px;line-height:20px;color:#444;text-align:center}
.btn{display:inline-block;background:var(--orange);color:var(--white);font-size:12px;font-weight:700;border-radius:20px;text-align:center;box-shadow:0 3px 8px rgba(247,148,29,.35)}
.hero .btn{left:771px;top:286px;width:118px;height:33px;line-height:33px}

/* features */
.features{left:42px;top:584px;width:1117px;height:248px;display:flex}
.feature{flex:1;text-align:center;color:var(--white);padding-top:52px}
.feature:nth-child(1){background:var(--orange)}
.feature:nth-child(2){background:var(--orange-2)}
.feature:nth-child(3){background:var(--orange-3)}
.feature:nth-child(4){background:var(--orange-4)}
.feature .ring{width:50px;height:50px;border-radius:50%;background:var(--white);margin:0 auto 14px;display:flex;align-items:center;justify-content:center}
.feature h3{font-size:20px;font-weight:700;margin-bottom:10px}
.feature p{font-size:11px;line-height:20px;width:190px;margin:0 auto}

/* why */
.sec-title{font-size:30px;font-weight:700;color:var(--ink)}
.why-title{left:0;width:1200px;top:905px}
.why-text{left:290px;width:620px;top:958px}
.doctor{left:432px;top:1013px;width:340px;height:418px;background:radial-gradient(ellipse at 50% 40%,#e9ecef 0%,#c8ced6 55%,#ffffff 100%);border-radius:170px 170px 0 0}
.point{width:250px}
.point .head{display:flex;align-items:center;gap:12px;margin-bottom:14px}
.point .ring{width:48px;height:48px;border-radius:50%;background:var(--orange);display:flex;align-items:center;justify-content:center;flex:none}
.point h4{font-size:21px;font-weight:600;color:#555}

/* stats */
.stats{left:42px;top:1431px;width:1117px;height:411px;background:linear-gradient(90deg,#f7941d 0%,#f9a237 45%,#e99a3f 70%,#f7941d 100%)}
.stat{width:200px;text-align:center;color:var(--white);top:100px}
.stat .num{font-size:40px;font-weight:500;margin-top:12px}
.stat .bar{width:50px;height:3px;background:var(--white);margin:12px auto 12px}
.stat .lbl{font-size:17px;line-height:21px}

/* how & creative */
.col-title{font-size:32px;font-weight:600;color:var(--ink)}
.photo-a{background:linear-gradient(135deg,#e2d8cf,#b9b2aa)}
.photo-b{background:linear-gradient(135deg,#d9e2ea,#8fa7bd)}
.post h5{font-size:12px;font-weight:600;color:var(--ink);margin-top:30px}
.post .date{font-size:9px;color:var(--orange);margin:6px 0 10px}
.pill{width:292px;height:36px;border-radius:18px;background:var(--pale);display:flex;align-items:center;gap:12px;padding-left:6px;font-size:13px;color:var(--ink)}
.pill .dot{width:25px;height:25px;border-radius:50%;background:var(--white);display:flex;align-items:center;justify-content:center}
.pill.on{background:var(--orange);color:var(--white)}

/* gallery */
.gallery{left:42px;top:2466px;width:1117px;height:576px;background:var(--dark)}
.gallery .tile{width:240px;height:145px}
.t1{background:linear-gradient(135deg,#e9edf1,#7b8794)}
.t2{background:linear-gradient(135deg,#d7d8de,#f0a97a)}
.t3{background:linear-gradient(135deg,#e6d7c4,#c49a78)}
.t4{background:linear-gradient(135deg,#eeeeee,#aab4bd)}
.t5{background:linear-gradient(135deg,#3c5364,#a8b6bf)}
.t6{background:linear-gradient(135deg,#8a8a8a,#2a2a2a)}

/* team */
.member{width:214px;text-align:center;top:3294px}
.member .pic{width:193px;height:193px;border-radius:50%;margin:0 auto 26px;background:radial-gradient(circle at 50% 40%,#f1f3f5,#a9b6c4)}
.member h6{font-size:17px;font-weight:500;color:#555}
.member p{font-size:11px;color:#555;margin:8px 0 16px}
.member .social{justify-content:center}

/* offer */
.offer{left:42px;top:3683px;width:1117px;height:120px;background:var(--pale)}
.offer h3{left:150px;top:47px;width:640px;font-size:21px;font-weight:600;color:#333;white-space:nowrap}
.offer .btn{left:828px;top:43px;width:134px;height:36px;line-height:36px;font-size:14px;font-weight:600}

/* footer */
.footer{left:42px;top:3803px;width:1117px;height:510px;background:var(--dark);color:#cfcfcf}
.footer h4{font-size:14px;font-weight:700;color:var(--white)}
.flist li{list-style:none;font-size:11px;line-height:27px;color:#cfcfcf;display:flex;align-items:center;gap:14px}
.flist li::before{content:"";border-left:5px solid var(--orange);border-top:4px solid transparent;border-bottom:4px solid transparent}
.contact{display:flex;gap:28px;align-items:flex-start;font-size:11px;line-height:16px}
.field{width:162px;border-bottom:1px solid #555;font-size:11px;color:#cfcfcf;padding-bottom:10px}
.copy{left:0;width:1117px;top:470px;text-align:center;font-size:9px;color:var(--orange)}
</style>
</head>
<body>

<!-- header -->
<div class="abs logo"><span class="mark"></span>Torven Medical</div>
<div class="abs info" style="left:477px">
  <div class="ico"><svg width="18" height="18" viewBox="0 0 18 18"><circle cx="9" cy="9" r="7" fill="none" stroke="#fff" stroke-width="2"/><path d="M9 5v4l3 2" stroke="#fff" stroke-width="2" fill="none"/></svg></div>
  <div><b>WORK TIME: 09:00 - 17:00</b><span>Saturday and Sunday - CLOSED</span></div>
</div>
<div class="abs info" style="left:717px">
  <div class="ico"><svg width="18" height="14" viewBox="0 0 18 14"><rect x="1" y="1" width="16" height="12" rx="1" fill="#fff"/><path d="M1 1l8 7 8-7" stroke="#f7941d" stroke-width="1.5" fill="none"/></svg></div>
  <div><b>MAIL US</b><span>info@torvenmedical.com</span></div>
</div>
<div class="abs info" style="left:902px">
  <div class="ico"><svg width="12" height="18" viewBox="0 0 12 18"><rect x="1" y="1" width="10" height="16" rx="2" fill="none" stroke="#fff" stroke-width="2"/><circle cx="6" cy="14" r="1" fill="#fff"/></svg></div>
  <div><b>CALL US</b><span>+100 5550 1200</span></div>
</div>
<div class="abs topline"></div>
<nav class="abs nav"><span class="active">Home</span><span>About</span><span>Products</span><span>Gallery</span><span>Blog</span><span>Contact us</span></nav>
<div class="abs social" style="left:872px;top:98px"><i></i><i></i><i></i><i></i><i></i></div>

<!-- hero -->
<section class="abs hero" role="img" aria-label="Surgeon holding a powered bone drill in a bright operating room">
  <h1 class="abs">Superior bone drills &amp; saws at lower cost</h1>
  <p class="abs">Orthopedic instruments of surgical grade quality, priced well below list for hospitals and surgeons.</p>
  <span class="abs btn">READ MORE</span>
</section>

<!-- features -->
<section class="abs features">
  <div class="feature"><div class="ring"><svg width="24" height="24" viewBox="0 0 24 24"><rect x="3" y="8" width="11" height="7" rx="2" stroke="#f7941d" stroke-width="2" fill="none"/><path d="M6 15v5h4v-5M14 11.5h7" stroke="#f7941d" stroke-width="2" fill="none"/></svg></div><h3>Bone Drills</h3><p>Cordless and corded drills with sealed motors, balanced grip and long battery life.</p></div>
  <div class="feature"><div class="ring"><svg width="24" height="24" viewBox="0 0 24 24"><path d="M3 15l12-12 4 4L7 19z" stroke="#f89f30" stroke-width="2" fill="none"/><path d="M6 12l2 2M9 9l2 2M12 6l2 2M7 19l-3 3" stroke="#f89f30" stroke-width="2"/></svg></div><h3>Bone Saws</h3><p>Sagittal and reciprocating saws that cut clean with low vibration in theatre.</p></div>
  <div class="feature"><div class="ring"><svg width="24" height="24" viewBox="0 0 24 24"><path d="M4 20L20 4M7 20L20 7" stroke="#f5a843" stroke-width="2" fill="none"/></svg></div><h3>K-Wires</h3><p>Stainless steel Kirschner wires in full sizes, sterile packed and ready to ship.</p></div>
  <div class="feature"><div class="ring"><svg width="24" height="24" viewBox="0 0 24 24"><path d="M12 3v14l-2 4M12 17l2 4M8 5h8" stroke="#f3b159" stroke-width="2" fill="none"/></svg></div><h3>Pins</h3><p>Steinmann and fixation pins made to tight tolerance at a fraction of list price.</p></div>
</section>

<!-- why choose us -->
<h2 class="abs sec-title why-title center">Why Choose Us ?</h2>
<p class="abs why-text small center">Torven Medical was founded to bring superb quality orthopedic instruments to surgeons and material managers at deeply discounted prices, without compromise on precision or safety.</p>
<div class="abs doctor" role="img" aria-label="Orthopedic surgeon in scrubs holding a bone saw"></div>
<div class="abs point" style="left:189px;top:1078px"><div class="head"><span class="ring"><svg width="22" height="22" viewBox="0 0 22 22"><path d="M11 3v16M7 7h6a3 3 0 010 6H9a3 3 0 000 6h6" stroke="#fff" stroke-width="2" fill="none"/></svg></span><h4>Cost Savings</h4></div><p class="small">Save up to half on drills, saws and wires compared with list prices.</p></div>
<div class="abs point" style="left:767px;top:1068px"><div class="head"><span class="ring"><svg width="22" height="22" viewBox="0 0 22 22"><path d="M4 11l5 5 9-10" stroke="#fff" stroke-width="2.4" fill="none"/></svg></span><h4>Superior Quality</h4></div><p class="small">Every instrument is tested for torque, speed and wear before it ships.</p></div>
<div class="abs point" style="left:189px;top:1262px"><div class="head"><span class="ring"><svg width="22" height="22" viewBox="0 0 22 22"><path d="M2 7h11v8H2zM13 10h4l3 3v2h-7" stroke="#fff" stroke-width="2" fill="none"/><circle cx="6" cy="17" r="2" fill="#fff"/><circle cx="16" cy="17" r="2" fill="#fff"/></svg></span><h4>Fast Supply</h4></div><p class="small">Stock held close to you, so your theatre lists never have to wait.</p></div>
<div class="abs point" style="left:767px;top:1262px"><div class="head"><span class="ring"><svg width="22" height="22" viewBox="0 0 22 22"><path d="M11 2l8 3v6c0 5-4 8-8 9-4-1-8-4-8-9V5z" stroke="#fff" stroke-width="2" fill="none"/></svg></span><h4>Full Warranty</h4></div><p class="small">Every power tool is covered, with repair and loan units on request.</p></div>

<!-- stats -->
<section class="abs stats" role="img" aria-label="Surgeon reviewing an x-ray under an orange tint">
  <div class="abs stat" style="left:216px"><svg width="64" height="52" viewBox="0 0 64 52"><path d="M26 4h12v10h10v12H38v10H26V26H16V14h10z" stroke="#fff" stroke-width="2.5" fill="none"/><path d="M4 30l10 14h14M60 30L50 44H36" stroke="#fff" stroke-width="2.5" fill="none"/></svg><div class="num">1000+</div><div class="bar"></div><div class="lbl">Hospitals<br>Supplied</div></div>
  <div class="abs stat" style="left:434px"><svg width="64" height="52" viewBox="0 0 64 52"><path d="M32 48S6 32 6 16a12 12 0 0126-4 12 12 0 0126 4c0 16-26 32-26 32z" stroke="#fff" stroke-width="2.5" fill="none"/><path d="M14 24h10l4-8 6 14 4-6h12" stroke="#fff" stroke-width="2.5" fill="none"/></svg><div class="num">2017</div><div class="bar"></div><div class="lbl">Year<br>Founded</div></div>
  <div class="abs stat" style="left:656px"><svg width="64" height="52" viewBox="0 0 64 52"><path d="M14 8h36M32 8v8M8 22h40a8 8 0 018 8v6H16l-8-14zM20 44h30M26 36v8M44 36v8" stroke="#fff" stroke-width="2.5" fill="none"/></svg><div class="num">1105</div><div class="bar"></div><div class="lbl">Instruments<br>In Stock</div></div>
</section>

<!-- how we works -->
<h2 class="abs col-title" style="left:189px;top:1905px">How we works</h2>
<p class="abs small" style="left:191px;top:1958px;width:500px">We source directly from certified makers, test each instrument in house and pass the savings on to surgeons and material managers. No middle layers, no inflated list prices.</p>
<div class="abs post" style="left:192px;top:2052px;width:235px">
  <div class="photo-a" style="height:146px" role="img" aria-label="Bone drill on a sterile instrument tray"></div>
  <h5>Choosing the right bone drill</h5><div class="date">April 19, 2019 &nbsp;|&nbsp; Dr. Elan Marsh</div>
  <p class="small">Speed, torque and weight: what matters most when your team selects a drill.</p>
</div>
<div class="abs post" style="left:455px;top:2052px;width:233px">
  <div class="photo-b" style="height:146px" role="img" aria-label="Surgeon preparing a sagittal bone saw"></div>
  <h5>Cutting costs, not quality</h5><div class="date">April 19, 2017 &nbsp;|&nbsp; Dr. Elan Marsh</div>
  <p class="small">How hospital buyers save on saws and wires while keeping every standard.</p>
</div>
<span class="abs btn" style="left:371px;top:2366px;width:108px;height:29px;line-height:29px;font-size:11px">READ MORE</span>

<!-- our products -->
<h2 class="abs col-title" style="left:731px;top:1905px">Our products</h2>
<p class="abs small" style="left:731px;top:1958px;width:290px">A focused range of orthopedic instruments, each built for daily theatre use and priced for tight hospital budgets.</p>
<div class="abs pill on" style="left:731px;top:2052px"><span class="dot"><svg width="8" height="10" viewBox="0 0 8 10"><path d="M1 1l6 4-6 4z" fill="#f7941d"/></svg></span>Bone Drills</div>
<p class="abs small" style="left:731px;top:2097px;width:290px">Cannulated and standard drills with quick change chucks, sealed for repeated sterilisation and backed by a full warranty at a lower price.</p>
<div class="abs pill" style="left:731px;top:2207px"><span class="dot"><svg width="8" height="10" viewBox="0 0 8 10"><path d="M1 1l6 4-6 4z" fill="#f7941d"/></svg></span>Bone Saws</div>
<div class="abs pill" style="left:731px;top:2253px"><span class="dot"><svg width="8" height="10" viewBox="0 0 8 10"><path d="M1 1l6 4-6 4z" fill="#f7941d"/></svg></span>K-Wires</div>
<div class="abs pill" style="left:731px;top:2299px"><span class="dot"><svg width="8" height="10" viewBox="0 0 8 10"><path d="M1 1l6 4-6 4z" fill="#f7941d"/></svg></span>Pins</div>

<!-- gallery -->
<section class="abs gallery">
  <h2 class="abs sec-title center" style="left:0;width:1117px;top:60px;color:#fff;font-size:31px">Gallery</h2>
  <p class="abs center" style="left:170px;width:777px;top:118px;font-size:11px;line-height:21px;color:#e6e6e6">A look at our drills, saws, wires and pins in the hands of the surgical teams who use them every day, from trauma bays to elective joint lists.</p>
  <div class="abs tile t1" style="left:181px;top:194px" role="img" aria-label="Cordless bone drill on a steel tray"></div>
  <div class="abs tile t2" style="left:445px;top:194px" role="img" aria-label="Sagittal saw blade close up"></div>
  <div class="abs tile t3" style="left:711px;top:194px" role="img" aria-label="Hands holding a knee joint model"></div>
  <div class="abs tile t4" style="left:181px;top:365px" role="img" aria-label="Set of K-wires and fixation pins"></div>
  <div class="abs tile t5" style="left:445px;top:365px" role="img" aria-label="Surgeons reviewing x-rays at a desk"></div>
  <div class="abs tile t6" style="left:711px;top:365px" role="img" aria-label="Instrument case with drill and saw"></div>
</section>

<!-- team -->
<h2 class="abs sec-title center" style="left:0;width:1200px;top:3136px;font-size:31px;font-weight:600">Our Team</h2>
<p class="abs small center" style="left:215px;width:770px;top:3198px">Our product specialists come from orthopedic theatres and hospital supply, so they know what surgeons and material managers need from every instrument.</p>
<div class="abs member" style="left:181px"><div class="pic" role="img" aria-label="Portrait of a team specialist"></div><h6>Dr Elan Marsh</h6><p>Assistant Surgeon</p><div class="social orange"><i></i><i></i><i></i></div></div>
<div class="abs member" style="left:395px"><div class="pic" role="img" aria-label="Portrait of a team specialist"></div><h6>Dr Elan Marsh</h6><p>Assistant Surgeon</p><div class="social orange"><i></i><i></i><i></i></div></div>
<div class="abs member" style="left:609px"><div class="pic" role="img" aria-label="Portrait of a team specialist"></div><h6>Dr Elan Marsh</h6><p>Assistant Surgeon</p><div class="social orange"><i></i><i></i><i></i></div></div>
<div class="abs member" style="left:824px"><div class="pic" role="img" aria-label="Portrait of a team specialist"></div><h6>Dr Elan Marsh</h6><p>Assistant Surgeon</p><div class="social orange"><i></i><i></i><i></i></div></div>

<!-- offer -->
<section class="abs offer">
  <h3 class="abs">New Hospital Accounts: Complimentary Trial Instrument</h3>
  <span class="abs btn">READ MORE</span>
</section>

<!-- footer -->
<footer class="abs footer">
  <h4 class="abs" style="left:150px;top:76px">Get in Touch</h4>
  <div class="abs contact" style="left:152px;top:132px"><svg width="26" height="20" viewBox="0 0 26 20"><rect x="1" y="1" width="24" height="18" fill="none" stroke="#aaa"/><path d="M1 1l12 10 12-10" fill="none" stroke="#aaa"/></svg><span>care@torvenmedical.com</span></div>
  <div class="abs contact" style="left:156px;top:198px"><svg width="18" height="28" viewBox="0 0 18 28"><rect x="1" y="1" width="16" height="26" rx="2" fill="none" stroke="#aaa"/><path d="M6 23h6" stroke="#aaa"/></svg><span style="margin-left:6px">+100 555 0134<br>+100 555 0134</span></div>
  <div class="abs contact" style="left:152px;top:268px"><svg width="26" height="30" viewBox="0 0 26 30"><path d="M13 22S5 13 5 9a8 8 0 0116 0c0 4-8 13-8 13z" fill="none" stroke="#aaa"/><circle cx="13" cy="9" r="3" fill="none" stroke="#aaa"/><path d="M2 29l5-7h12l5 7z" fill="none" stroke="#aaa"/></svg><span>48, Harbor Lane, Westfield,<br>Northland 20418</span></div>
  <div class="abs social white" style="left:156px;top:353px;gap:22px"><i></i><i></i><i></i><i></i><i></i></div>

  <h4 class="abs" style="left:403px;top:76px">Quick Links</h4>
  <ul class="abs flist" style="left:414px;top:121px"><li>About us</li><li>Products</li><li>Blog</li><li>Faq</li><li>Warranty</li><li>Contact us</li></ul>

  <h4 class="abs" style="left:596px;top:76px">Our Products</h4>
  <ul class="abs flist" style="left:598px;top:121px"><li>Bone Drills</li><li>Bone Saws</li><li>Saw Blades</li><li>K-Wires</li><li>Steinmann Pins</li><li>Instrument Repair</li></ul>

  <h4 class="abs" style="left:818px;top:76px">Enquiry Form</h4>
  <div class="abs field" style="left:820px;top:127px">Name</div>
  <div class="abs field" style="left:820px;top:167px">Phone</div>
  <div class="abs field" style="left:820px;top:207px;height:60px">Message</div>
  <span class="abs btn" style="left:822px;top:290px;width:87px;height:22px;line-height:22px;font-size:8px">SUBMIT</span>

  <div class="abs copy">Copyright © 2019. Torven Medical</div>
</footer>

</body>
</html>
```